We need a web site design that is connected to Ridgeway Roofing an American company, Veteran owned. Specializing in new roofs of all kinds, repair existing roofs and emergency roof repairs. located in the north Georgia mountains

Target Market(s)

homeowners end users, real estate, home owners insurance companies

Industry/Entity Type

roofing

Contact Information for Business Card

logo, Veteran owned, supports veteran charities, phone number ect

Font styles to use
Serif

Requirements
Should not have
• na

```html
<!DOCTYPE html>
<html lang="en">
<head>
<meta charset="utf-8">
<title>Ridgeway Roofing – Business Card</title>
<link rel="stylesheet" href="https://fonts.googleapis.com/css2?family=Poppins:wght@400;500;600&display=swap">
<style>
  :root {
    --backdrop: #6c6c6c;
    --card: #ffffff;
    --brand-red: #d8280f;
    --band-red: #d9300c;
    --gold: #e2a92a;
    --ink: #3a3a3a;
    --navy: #1d2c57;
  }
  * { box-sizing: border-box; margin: 0; padding: 0; }
  html, body {
    width: 1093px; height: 1200px; overflow: hidden;
    background: var(--backdrop);
    font-family: "Poppins", sans-serif;
  }
  .card {
    position: absolute; left: 264px; width: 578px; height: 357px;
    background: var(--card); border-radius: 22px; overflow: hidden;
    box-shadow: 3px 4px 6px rgba(0,0,0,.45);
  }
  .card--front { top: 226px; }
  .card--back { top: 621px; left: 264px; width: 582px; }
  .card__band {
    position: absolute; left: 0; bottom: 0; width: 100%; height: 40px;
  }
  .person { position: absolute; left: 27px; top: 32px; }
  .person__name {
    color: var(--gold); font-size: 21px; font-weight: 500;
    letter-spacing: 1.6px; line-height: 1; white-space: nowrap;
  }
  .person__role { color: var(--brand-red); font-size: 17px; line-height: 1.2; margin-top: 1px; }
  .address {
    position: absolute; left: 27px; top: 193px;
    color: var(--ink); font-size: 17px; line-height: 21px;
  }
  .contacts { position: absolute; left: 27px; top: 260px; list-style: none; }
  .contacts li {
    display: flex; align-items: center; gap: 7px;
    color: var(--ink); font-size: 17px; line-height: 21px; white-space: nowrap;
  }
  .contacts svg { width: 15px; height: 15px; flex: none; }
  .contacts .accent { color: var(--brand-red); }
  .brand-name {
    position: absolute; text-align: center; color: var(--brand-red);
    font-weight: 600; text-transform: uppercase; line-height: 1.05;
  }
  .card--front .brand-name { left: 318px; top: 96px; width: 232px; font-size: 34px; }
  .card--back .brand-name { left: 0; top: 108px; width: 100%; font-size: 54px; }
  .veteran-badge {
    position: absolute; left: 433px; top: 253px; width: 126px; height: 70px;
    background: linear-gradient(135deg, #b8323a 0%, #e9e9ee 45%, var(--navy) 100%);
  }
</style>
</head>
<body>
  <section class="card card--front">
    <div class="person">
      <p class="person__name">DANIEL HARPER</p>
      <p class="person__role">Managing Director</p>
    </div>

    <p class="brand-name">Ridgeway<br>Roofing</p>

    <p class="address">421, Address line goes here<br>45452,Country Name</p>

    <ul class="contacts">
      <li>
        <svg viewBox="0 0 16 16" aria-hidden="true"><path fill="#d8280f" d="M3.5 1.5l2.3 2.8-1.4 1.6c.9 2 2.6 3.7 4.6 4.6l1.6-1.4 2.8 2.3-1.5 2.1C6.7 13.4 2.6 9.3 1.4 3z"/><path fill="none" stroke="#d8280f" stroke-width="1.2" d="M9.5 2.5a4 4 0 0 1 4 4M9.5 0.8a5.7 5.7 0 0 1 5.7 5.7"/></svg>
        706-555 014 233
      </li>
      <li>
        <svg viewBox="0 0 16 16" aria-hidden="true"><rect x="0.5" y="3" width="15" height="10" fill="#d8280f"/><path fill="none" stroke="#fff" stroke-width="1.2" d="M1 3.5l7 5.5 7-5.5M1 12.5l5-4.5M15 12.5l-5-4.5"/></svg>
        info@ridgeway.com
      </li>
      <li>
        <svg viewBox="0 0 16 16" aria-hidden="true"><g fill="none" stroke="#d8280f" stroke-width="1.3"><circle cx="8" cy="8" r="7"/><ellipse cx="8" cy="8" rx="3" ry="7"/><path d="M1 8h14M2.2 4.3h11.6M2.2 11.7h11.6"/></g></svg>
        <span>www.<span class="accent">ridgewayroofs</span>.com</span>
      </li>
    </ul>

    <div class="veteran-badge" role="img" aria-label="Veteran owned business badge"></div>

    <svg class="card__band" viewBox="0 0 578 40" preserveAspectRatio="none" aria-hidden="true">
      <path fill="var(--band-red)" d="M0 27h276l22-20 22 20h258v13H0z"/>
      <path fill="none" stroke="#f7b98a" stroke-width="1.5" d="M287 21l11-9 11 9"/>
    </svg>
  </section>

  <section class="card card--back">
    <p class="brand-name">Ridgeway<br>Roofing</p>
    <svg class="card__band" viewBox="0 0 582 40" preserveAspectRatio="none" aria-hidden="true">
      <path fill="var(--band-red)" d="M0 27h280l22-20 22 20h258v13H0z"/>
      <path fill="none" stroke="#f7b98a" stroke-width="1.5" d="M291 21l11-9 11 9"/>
    </svg>
  </section>
</body>
</html>
```